Unique Builder wordpress website - Supply Graphics Only

We need a brand new website for a building company in Perth, Australia who constructs insulated panels (sip).
What is a SIP?
A SIP is a high-performance building panel used for floors, walls, and roofs in residential and commercial buildings. Panels are typically made using Expanded Polystyrene (EPS) sandwiched between two structural skins.
The design must incorporate a slick professional look and keep to the logo colours (Lime green & Blacks). The logo must not change colours or be altered. (
We will convert the graphics to a wordpress site. We have our own coders)
Design:
The website design must be clean, mobile friendly and the final design will be adapted to WordPress CMS.
The menus must contain dropdown menus and front page may contain a youtube video at a later date.
Fonts must be clear and easy to read
The contact us page will need to have an online form and google map.
The 16 pages listed will be the complete site and are for reference only. For this project the winning designer would need to supply the Homepage, and 1 inner pages only as PSD files.
The structure is as follows:
Home
About us
High Tech Homes
What is a sip
Benefits
FAQ
Designs
Residential
Granny Flats
Architectural design
Photo Gallery <--- Would be great if a sample design can be provided
Services
Project management and custom design
Site Assembly
Kit Supply
Contact us
***We don't need the designer to design every page however a 1 inner page would be ideal****
Our Competitors websites
Note: the following websites look crap however, the following websites are some of our competitors. We want a clean and awesome layout.
http://www.vortmelbuild.com.au/
http://kelvarostructures.com.au/
http://www.tralinbowerk.net.au/
New home builders and commercial builders
Building
5+ page

```html
<!DOCTYPE html>
<html lang="en">
<head>
<meta charset="utf-8">
<title>PanelForm – Advanced Building Technology</title>
<link href="https://fonts.googleapis.com/css2?family=Ubuntu:wght@400;500;700&family=Open+Sans:wght@400;600&display=swap" rel="stylesheet">
<style>
:root{
  --lime:#a6cf2c;
  --lime-light:#bde24a;
  --lime-dark:#8db81c;
  --ink:#2e2e2e;
  --text:#555;
  --muted:#777;
  --rule:#d9d9d9;
  --footer:#3b3b3b;
  --white:#fff;
}
*{margin:0;padding:0;box-sizing:border-box}
html,body{width:1012px;height:1200px;overflow:hidden;background:var(--white)}
body{position:relative;font-family:"Open Sans",sans-serif;color:var(--text)}
.top-line{position:absolute;left:0;top:0;width:1012px;height:3px;background:var(--lime)}
.brand{position:absolute;left:111px;top:24px;display:flex;align-items:center;gap:8px}
.brand-mark{width:20px;height:20px;background:var(--ink)}
.brand-name{font-family:"Ubuntu",sans-serif;font-weight:500;font-size:26px;color:var(--ink);letter-spacing:-.5px}
.brand-tag{position:absolute;left:111px;top:58px;font-size:7px;font-weight:600;color:var(--ink);letter-spacing:.3px}
.enquiries{position:absolute;right:111px;top:26px;display:flex;align-items:center;font-size:10px;color:var(--ink)}
.enquiries .label{margin-right:12px}
.icon-dot{width:24px;height:24px;border-radius:50%;background:var(--lime);display:flex;align-items:center;justify-content:center;margin-right:8px}
.enquiries .phone{margin-right:14px}
.top-nav{position:absolute;right:111px;top:64px;font-size:10px;color:var(--ink);display:flex}
.top-nav span{padding:0 7px}
.top-nav span.sep{padding:0}
.top-nav .active{color:var(--lime)}
.top-nav span:last-child{padding-right:0}
.main-nav{position:absolute;left:0;top:97px;width:1012px;height:38px;background:linear-gradient(var(--lime-light),var(--lime))}
.main-nav ul{list-style:none;display:flex;position:absolute;left:111px;top:0;height:38px}
.main-nav li{height:38px;line-height:38px;font-size:10px;color:var(--white);padding:0 14px;border-right:1px solid rgba(255,255,255,.35)}
.main-nav li:last-child{border-right:none}
.main-nav li.current{background:var(--lime-dark)}
.hero{position:absolute;left:111px;top:157px;width:790px;height:361px;background:#353535;overflow:hidden}
.hero-art{position:absolute;right:0;top:0;width:520px;height:361px;background:radial-gradient(ellipse at 65% 50%,#c9a24a 0%,#6a4a6a 35%,#2a3050 65%,#353535 100%)}
.hero-copy{position:absolute;left:33px;top:98px}
.hero-kicker{font-family:"Ubuntu",sans-serif;font-size:17px;color:var(--white)}
.hero-title{font-family:"Ubuntu",sans-serif;font-weight:700;font-size:29px;color:var(--lime);margin-top:6px}
.hero-text{font-size:10px;line-height:16px;color:#bbb;width:230px;margin-top:8px}
.btn{display:inline-block;margin-top:18px;background:var(--lime);color:var(--white);font-family:"Ubuntu",sans-serif;font-weight:700;font-size:11px;letter-spacing:.5px;padding:9px 14px;border-radius:2px}
.dots{display:flex;gap:7px;margin-top:24px;margin-left:5px}
.dots i{width:4px;height:4px;border-radius:50%;background:var(--white)}
.dots i.on{background:var(--lime)}
.shadow{position:absolute;height:20px;background:radial-gradient(ellipse at 50% 0%,rgba(0,0,0,.25),rgba(0,0,0,0) 70%)}
.section-title{position:absolute;left:0;width:1012px;text-align:center;top:550px;font-family:"Ubuntu",sans-serif;font-size:25px;color:var(--ink)}
.service{position:absolute;top:608px;width:242px}
.service .photo{height:132px}
.service .band{height:48px;background:linear-gradient(var(--lime-light),var(--lime));color:var(--white);font-family:"Ubuntu",sans-serif;font-size:16px;line-height:48px;padding-left:14px}
.divider{position:absolute;left:111px;top:832px;width:790px;height:1px;background:var(--rule)}
.h2{position:absolute;font-family:"Ubuntu",sans-serif;font-size:25px;color:var(--ink);top:856px}
.welcome-copy{position:absolute;left:111px;top:898px;width:412px;font-size:10px;line-height:16px;color:var(--muted)}
.welcome-copy p{margin-bottom:16px}
.benefits{list-style:none;margin-top:28px}
.benefits li{color:var(--lime-dark);font-size:10.5px;line-height:20px;padding-left:18px;position:relative}
.benefits li::before{content:"›";position:absolute;left:2px;top:0}
.video{position:absolute;left:543px;top:903px;width:358px;height:211px;background:linear-gradient(135deg,#d9d4c7,#eef0f2 45%,#c9cfd6);overflow:hidden}
.video-actions{position:absolute;right:8px;top:8px;display:flex;flex-direction:column;gap:4px}
.video-actions div{width:31px;height:23px;background:#2f3a3a;border-radius:2px;color:var(--white);font-size:5px;text-align:center;padding-top:3px}
.video-bar{position:absolute;left:13px;bottom:7px;right:8px;height:24px;display:flex;gap:5px}
.play{width:38px;height:24px;background:#2f3a3a;border-radius:2px;display:flex;align-items:center;justify-content:center}
.track{flex:1;background:#2f3a3a;border-radius:2px;display:flex;align-items:center;padding:0 8px;gap:10px}
.progress{flex:1;height:6px;background:#666;position:relative}
.progress b{position:absolute;left:0;top:0;height:6px;width:32%;background:var(--lime)}
.hd{color:var(--lime);font-family:"Ubuntu",sans-serif;font-weight:700;font-style:normal;font-size:9px}
.footer{position:absolute;left:0;top:1146px;width:1012px;height:54px;background:var(--footer)}
.footer .copy{position:absolute;left:113px;top:20px;font-size:10px;color:#ccc}
.social{position:absolute;right:111px;top:20px;display:flex;gap:8px}
.social span{width:15px;height:15px;border-radius:2px}
</style>
</head>
<body>
<div class="top-line"></div>

<div class="brand"><span class="brand-mark"></span><span class="brand-name">PanelForm</span></div>
<div class="brand-tag">ADVANCED BUILDING TECHNOLOGY</div>

<div class="enquiries">
  <span class="label">For all your Enquiries</span>
  <span class="icon-dot"><svg width="11" height="11" viewBox="0 0 24 24"><path fill="#fff" d="M6.6 10.8a15.1 15.1 0 0 0 6.6 6.6l2.2-2.2c.3-.3.7-.4 1-.2 1.1.4 2.3.6 3.6.6.6 0 1 .4 1 1V20c0 .6-.4 1-1 1A17 17 0 0 1 3 4c0-.6.4-1 1-1h3.5c.6 0 1 .4 1 1 0 1.3.2 2.5.6 3.6.1.3 0 .7-.2 1z"/></svg></span>
  <span class="phone">1800-555-019</span>
  <span class="icon-dot"><svg width="11" height="11" viewBox="0 0 24 24"><rect x="3" y="5" width="18" height="14" rx="2" fill="none" stroke="#fff" stroke-width="2.2"/><path d="M3 7l9 6 9-6" fill="none" stroke="#fff" stroke-width="2.2"/></svg></span>
  <span>hello@panelform-mail.com</span>
</div>

<nav class="top-nav">
  <span class="active">Home</span><span class="sep">|</span><span>About us</span><span class="sep">|</span><span>High Tech Homes</span><span class="sep">|</span><span>What is a sip</span><span class="sep">|</span><span>Benefits</span><span class="sep">|</span><span>FAQ</span><span class="sep">|</span><span>Contact us</span>
</nav>

<nav class="main-nav"><ul>
  <li class="current">Designs</li><li>Residential</li><li>Granny Flats</li><li>Architectural design</li><li>Photo Gallery</li><li>Project management and custom design</li><li>Site Assembly</li><li>Kit Supply</li>
</ul></nav>

<section class="hero">
  <div class="hero-art" role="img" aria-label="Businessman holding a glowing holographic wireframe of city towers"></div>
  <div class="hero-copy">
    <div class="hero-kicker">Get Your Free</div>
    <div class="hero-title">SIPS Info Pack</div>
    <p class="hero-text">panelform are designers and manufacturers of an engineered structural insulated</p>
    <span class="btn">Enquiry Now</span>
    <div class="dots"><i class="on"></i><i></i><i></i></div>
  </div>
</section>
<div class="shadow" style="left:190px;top:518px;width:632px"></div>

<h2 class="section-title">Our Services</h2>

<div class="service" style="left:111px">
  <div class="photo" role="img" aria-label="Builders fitting insulated panels inside a timber frame" style="background:linear-gradient(135deg,#b98a57,#d9b07c 50%,#8d6a48)"></div>
  <div class="band">Custom Design</div>
</div>
<div class="service" style="left:385px">
  <div class="photo" role="img" aria-label="Two-storey panel house under construction against a winter sky" style="background:linear-gradient(180deg,#9fb6cf,#c9b48f 55%,#8e8270)"></div>
  <div class="band">Residential</div>
</div>
<div class="service" style="left:657px">
  <div class="photo" role="img" aria-label="Worker cutting a panel with a power tool in a workshop" style="background:linear-gradient(135deg,#7a5a48,#3e4e6a 50%,#a08870)"></div>
  <div class="band">Commercial</div>
</div>
<div class="shadow" style="left:125px;top:788px;width:214px"></div>
<div class="shadow" style="left:399px;top:788px;width:214px"></div>
<div class="shadow" style="left:671px;top:788px;width:214px"></div>

<div class="divider"></div>

<h2 class="h2" style="left:113px">Welcome to Panelform</h2>
<div class="welcome-copy">
  <p>panelform are designers and manufacturers of an engineered structural insulated panel and concealed structural frame building product.</p>
  <p>sips is rapidly becoming the building method of choice because of its overwhelming benefits and proven suitability.</p>
  <ul class="benefits">
    <li>High level of captive insulation. (warm in winter cool in summer)</li>
    <li>Very strong, light weight and durable.</li>
    <li>20 + year history of performance in cyclonic locations in WA</li>
    <li>Reduced build time (save time save money it's that easy)</li>
    <li>Energy efficient ( less energy to build and less energy to run ie lower power bills)</li>
  </ul>
</div>

<h2 class="h2" style="left:545px">Watch our Video</h2>
<div class="video">
  <div role="img" aria-label="Architects' hands sketching house plans beside colour swatches and a calculator" style="position:absolute;inset:0"></div>
  <div class="video-actions"><div>LIKE</div><div>LATER</div><div>SHARE</div><div>EMBED</div></div>
  <div class="video-bar">
    <div class="play"><svg width="8" height="9" viewBox="0 0 8 9"><path d="M0 0l8 4.5L0 9z" fill="#fff"/></svg></div>
    <div class="track"><div class="progress"><b></b></div><span class="hd">HD</span></div>
  </div>
</div>

<footer class="footer">
  <div class="copy">© 2016 PanelForm, Perth - All right Reserved.</div>
  <div class="social">
    <span style="background:#3b5a9a" aria-label="Social profile"></span>
    <span style="background:#3aa6d8" aria-label="Social profile"></span>
    <span style="background:#e8892b" aria-label="News feed"></span>
  </div>
</footer>
</body>
</html>
```